Vibrant Body Mist Fine fragance

Hello

I need 6 body mists designs.
The designs should be colorful, with great background, shocking so that people can fall in love with the product just by seeing it. The label design will be the selling point of the fragrance.
6 names are:
Amber Twilight
Plum Whisper
Lush Peachy
Andean Guava
Capri Melon
Sela Sela Dusk

Names could change if you have a better idea or a more touchy name
Label should include:
Fine Fragrance Mist
250 ml / 8.45oz

Ideas of body mists in the attachment

Women all ages

• Fine Fragrance Mist
• 250ml / 8.45 oz
• Name of the fragrance should be the focus point
• Fruits, Paradise Background, Colors, Name of the fragrance should be the focus point

```html
<!DOCTYPE html>
<html lang="en">
<head>
<meta charset="UTF-8">
<title>Sela Sela Dusk – Fine Fragrance Mist</title>
<link href="https://fonts.googleapis.com/css2?family=Great+Vibes&family=Cormorant+Garamond:wght@500&display=swap" rel="stylesheet">
<style>
  :root {
    --sun-yellow: #f7ec6a;
    --warm-orange: #f29a4a;
    --hot-pink: #e23a8c;
    --magenta: #b81e7a;
    --violet: #6a2c9c;
    --deep-purple: #3a1466;
    --leaf-green: #2f9a5a;
    --teal: #1f8f8a;
    --glow-white: #fff8ec;
    --cream-text: #fbf1d6;
    --gold-shadow: #6b4a12;
    --frame-line: #5a3a3a;
  }
  * { margin: 0; padding: 0; box-sizing: border-box; }
  html, body {
    width: 1200px;
    height: 2400px;
    overflow: hidden;
    background: #ffffff;
  }
  .label {
    position: relative;
    width: 1200px;
    height: 2400px;
    overflow: hidden;
  }
  .paradise-backdrop {
    position: absolute;
    inset: 0;
    background:
      radial-gradient(ellipse 520px 600px at 120px 260px, var(--sun-yellow) 0%, rgba(247,236,106,0) 70%),
      radial-gradient(ellipse 700px 520px at 820px 260px, var(--glow-white) 0%, rgba(255,248,236,0) 65%),
      radial-gradient(ellipse 500px 700px at 1120px 1500px, var(--teal) 0%, rgba(31,143,138,0) 70%),
      radial-gradient(ellipse 600px 600px at 1100px 2300px, var(--leaf-green) 0%, rgba(47,154,90,0) 70%),
      radial-gradient(ellipse 600px 700px at 80px 2200px, var(--violet) 0%, rgba(106,44,156,0) 70%),
      radial-gradient(ellipse 600px 800px at 200px 1400px, var(--warm-orange) 0%, rgba(242,154,74,0) 70%),
      radial-gradient(ellipse 900px 900px at 600px 1900px, var(--glow-white) 0%, rgba(255,248,236,0) 55%),
      linear-gradient(160deg, var(--hot-pink) 0%, var(--magenta) 45%, var(--deep-purple) 100%);
  }
  .name-oval {
    position: absolute;
    left: 0;
    top: 0;
    width: 1200px;
    height: 2400px;
  }
  .fragrance-name {
    position: absolute;
    left: 0;
    width: 1200px;
    text-align: center;
    font-family: "Great Vibes", cursive;
    font-weight: 400;
    color: var(--cream-text);
    text-shadow:
      3px 3px 0 var(--gold-shadow),
      6px 8px 10px rgba(60, 30, 0, 0.55);
    line-height: 1;
  }
  .fragrance-name .line-one { position: absolute; left: 0; width: 100%; top: 740px; font-size: 200px; }
  .fragrance-name .line-two { position: absolute; left: 0; width: 100%; top: 1090px; font-size: 200px; }
  .product-type {
    position: absolute;
    left: 0;
    width: 1200px;
    top: 2050px;
    text-align: center;
    font-family: "Great Vibes", cursive;
    font-size: 92px;
    color: #ffffff;
    text-shadow: 2px 2px 4px rgba(40, 10, 60, 0.6);
  }
  .volume {
    position: absolute;
    left: 0;
    width: 1200px;
    top: 2155px;
    text-align: center;
    font-family: "Cormorant Garamond", serif;
    font-weight: 500;
    font-size: 62px;
    letter-spacing: 2px;
    color: #ffffff;
    text-shadow: 2px 2px 4px rgba(40, 10, 60, 0.6);
  }
</style>
</head>
<body>
  <main class="label">
    <div class="paradise-backdrop" role="img" aria-label="Vibrant abstract tropical swirl background in yellow, pink, magenta, teal and purple"></div>

    <svg class="name-oval" viewBox="0 0 1200 2400" xmlns="http://www.w3.org/2000/svg" role="img" aria-label="Oval window with glowing pink, orange and green abstract floral swirls">
      <defs>
        <radialGradient id="ovalGlow" cx="0.5" cy="0.35" r="0.75">
          <stop offset="0%" stop-color="#fff6e0"/>
          <stop offset="25%" stop-color="#f6b070"/>
          <stop offset="55%" stop-color="#e0458f"/>
          <stop offset="80%" stop-color="#b0206f"/>
          <stop offset="100%" stop-color="#3f8f5a"/>
        </radialGradient>
      </defs>
      <ellipse cx="600" cy="1074" rx="412" ry="866" fill="url(#ovalGlow)" opacity="0.9"/>
      <ellipse cx="600" cy="1074" rx="412" ry="866" fill="none" stroke="var(--frame-line)" stroke-width="5" stroke-dasharray="14 8"/>
    </svg>

    <h1 class="fragrance-name">
      <span class="line-one">Sela Sela</span>
      <span class="line-two">Dusk</span>
    </h1>

    <p class="product-type">Fine Fragrance Mist</p>
    <p class="volume">250 ML / 8.5 OZ</p>
  </main>
</body>
</html>
```